Kalm to Bloom: Prespective and Balence in People's Lives Needs a Buissness Card Design

Calm to Bloom Community Center is an organization that seeks to bring balance into people's lives. Main services include: guided meditation, group brainstorming, and guided counseling. Calm to Bloom combines Eastern practices, i.e. Buddhism, Hinduism, and Taoism, with Western practices: therapy, group brainstorming and healing. We would like a double sided card: 1) front vertical with image, 2) back horizontal with information. The main colors for the card are red, white, black. Different finishes would be nice--please no high gloss. Matte, pearlized, embossing--used tactfully and sparingly would be nice. The card should convey balance/harmony in a modern world.

```html
<!DOCTYPE html>
<html lang="en">
<head>
<meta charset="utf-8">
<title>Calm to Bloom Community Center – Business Card</title>
<link rel="stylesheet" href="https://fonts.googleapis.com/css2?family=Sorts+Mill+Goudy&display=swap">
<style>
  :root {
    --backdrop: #e9e5df;
    --paper: #ffffff;
    --ink: #1c1c1c;
    --ink-soft: #3a3a3a;
    --red: #d80f24;
    --red-faint: rgba(216, 15, 36, 0.16);
    --night: #0b0b0b;
  }
  * { box-sizing: border-box; margin: 0; padding: 0; }
  html, body {
    width: 1200px; height: 1023px; overflow: hidden;
    background: var(--backdrop);
    font-family: "Sorts Mill Goudy", Georgia, serif;
    color: var(--ink);
  }
  .sheet {
    position: relative; width: 1200px; height: 1023px;
  }
  .card {
    position: absolute;
    background: var(--paper);
    box-shadow: 0 10px 28px rgba(0,0,0,0.18);
    overflow: hidden;
  }

  /* Information side (horizontal) */
  .card-info {
    left: 70px; top: 250px; width: 600px; height: 343px;
    padding: 34px 38px;
  }
  .card-info .faint-mark {
    position: absolute; width: 120px; height: 120px; border-radius: 50%;
    background: var(--red-faint);
  }
  .card-info .faint-mark.top { right: 36px; top: 22px; }
  .card-info .faint-mark.bottom { left: 40px; bottom: 22px; }
  .brand {
    position: relative;
    font-size: 40px; line-height: 1; color: var(--red);
  }
  .center-name {
    position: relative;
    font-size: 30px; line-height: 1.2; color: var(--ink); margin-top: 6px;
  }
  .motto {
    position: relative;
    font-size: 15px; letter-spacing: 0.9em; text-transform: none;
    color: var(--ink); margin-top: 10px;
  }
  .person {
    position: absolute; left: 250px; top: 168px; width: 300px;
  }
  .person-name {
    font-size: 30px; color: var(--red); letter-spacing: 0.02em;
  }
  .person-role {
    font-size: 16px; letter-spacing: 0.35em; color: var(--ink-soft); margin-top: 2px;
  }
  .rule {
    height: 2px; background: var(--red); margin: 10px 0 12px; width: 290px;
  }
  .contact {
    list-style: none; font-size: 14px; line-height: 1.5; color: var(--ink-soft);
  }

  /* Image side (vertical) */
  .card-front {
    left: 800px; top: 250px; width: 300px; height: 525px;
    display: flex;
  }
  .card-front .half-light { flex: 1; background: var(--paper); }
  .card-front .half-dark { flex: 1; background: var(--night); }
  .front-mark {
    position: absolute; left: 50%; top: 50%; transform: translate(-50%, -50%);
    display: flex; flex-direction: column; align-items: center; gap: 14px;
  }
  .front-mark .dot {
    width: 110px; height: 110px; border-radius: 50%; background: var(--red);
  }
  .front-mark .word {
    font-size: 30px; color: var(--red); white-space: nowrap;
  }
</style>
</head>
<body>
<main class="sheet">
  <section class="card card-info" aria-label="Business card, information side">
    <span class="faint-mark top"></span>
    <span class="faint-mark bottom"></span>
    <h1 class="brand">Calm to Bloom</h1>
    <p class="center-name">Community Center</p>
    <p class="motto">Business Motto</p>
    <div class="person">
      <p class="person-name">YOUR NAME</p>
      <p class="person-role">Your Position</p>
      <div class="rule"></div>
      <ul class="contact">
        <li>000 000 0000</li>
        <li>yourmail@calmtobloom.com</li>
        <li>www.calmtobloom.com</li>
        <li>www.yourblog.com</li>
      </ul>
    </div>
  </section>

  <section class="card card-front" aria-label="Business card, image side">
    <div class="half-light"></div>
    <div class="half-dark"></div>
    <div class="front-mark">
      <span class="dot"></span>
      <span class="word">Calm to Bloom</span>
    </div>
  </section>
</main>
</body>
</html>
```